Business Card Design

I am in the progress of starting up my business.

Business Name - KT Surface Cleaning

Services that we offer
- Driveway Cleaning
- Foot Path Cleaning
- Pebble & Normal Cement
- Gutter Clean Out
- Removal of Moss & Mould
- Moss & Mould treatment is also available
- Entertainment & Courtyard Area's etc
- Gutter Guard Installation
- Full roof restoration, We Only Use Veltrano Products
- (veltrano application licence, Includes a full 10 year full warrenty )

New Business Card Information - I would like to get rid of "We cover all maitland & Newcastle regions" And Change it to Newcastle Region Hunter Valley Region Nelson Bay Region And the List on the back I would also like to change to OUR SERVICES Driveway & Foot Path Cleaning Treatment & Removal Of Moss & Mould Entertainment & Deck Area's Pebble Crete & cemented Area's Factory & Office Fronts House Exterior (Windows, Veranda's, Brick Work) Roof & Gutter Cleaning Roof Restoration - Veltrano, Korvin Roof Membrane 418 (Veltrano Application Licence, Includes Full 10 Year Warranty)

Industry/Entity Type

Business

Contact Information for Business Card

KT Surface Washing
Water Blasting And Roof Restorations
ABN # 47 219 806 153
Phone # 0417385926
Contact Reid For A Free Quote
Cover Maitland & Newcastle Region's

[Can you please send me an email when you would like me to send through picture as this page wont allow me to add pictures]

Thanks Reid

Requirements
Must have
• Main details on the front of the business card and a picture or two. on the back of the business I would like the list of services that my company provide on the back
Nice to have
• I was hoping that on the front of the business I could have all the company information and details and maybe a picture or two if able to. On the back of the card I would like the services I provide listed but also not over crowded at the same time..

```html
<!DOCTYPE html>
<html lang="en">
<head>
<meta charset="utf-8">
<title>KT Surface Washing – Business Card</title>
<link rel="stylesheet" href="https://fonts.googleapis.com/css2?family=Jura:wght@500;700&family=Short+Stack&display=swap">
<style>
  :root {
    --backdrop: #dcdcdc;
    --card-black: #0b0b0c;
    --card-charcoal: #2b2b2e;
    --ink-white: #f4f4f4;
    --ink-grey: #8d8d92;
    --accent-purple: #4b2a86;
    --tick-purple: #8e7ad6;
    --cloud-white: #ffffff;
    --photo-dark: #1c1c1e;
    --photo-mid: #5a5a5e;
  }
  * { margin: 0; padding: 0; box-sizing: border-box; }
  html, body { width: 1200px; height: 750px; overflow: hidden; }
  body {
    background: radial-gradient(ellipse at 50% 40%, #ececec 0%, var(--backdrop) 70%);
    font-family: "Jura", sans-serif;
    position: relative;
  }
  .card {
    position: absolute;
    top: 225px;
    width: 540px;
    height: 300px;
    border-radius: 22px;
    overflow: hidden;
    background: linear-gradient(120deg, var(--card-black) 0%, var(--card-black) 45%, var(--card-charcoal) 100%);
    color: var(--ink-white);
    box-shadow: 0 10px 24px rgba(0,0,0,0.25);
  }
  .card--services { left: 40px; }
  .card--front { left: 620px; }

  .photo { position: absolute; }
  .photo--foam-car {
    right: 0; top: 0; width: 240px; height: 230px;
    background: radial-gradient(ellipse closest-side at 55% 45%, #bfbfc2 0%, var(--photo-mid) 40%, rgba(28,28,30,0.6) 75%, rgba(28,28,30,0) 100%);
  }
  .photo--muddy-car {
    left: 0; top: 80px; width: 270px; height: 220px;
    background: radial-gradient(ellipse closest-side at 40% 60%, #7a7266 0%, #4a463f 40%, rgba(28,28,30,0.6) 75%, rgba(28,28,30,0) 100%);
  }

  .bubble { position: absolute; }
  .bubble text {
    font-family: "Short Stack", cursive;
    fill: #1a1a1a;
  }

  .business-title {
    position: absolute;
    top: 26px; left: 150px;
    width: 300px;
    text-align: center;
    font-weight: 700;
    font-size: 17px;
    line-height: 1.15;
  }
  .abn {
    position: absolute;
    top: 70px; right: 30px;
    font-size: 10px;
    color: var(--ink-grey);
  }
  .phone {
    position: absolute;
    top: 196px; left: 40px;
    display: flex; align-items: center; gap: 10px;
    font-size: 30px;
    font-weight: 500;
  }
  .phone-icon { width: 26px; height: 26px; }
  .contact-lines {
    position: absolute;
    top: 240px; left: 40px;
    font-size: 16px;
    line-height: 1.2;
    color: var(--ink-grey);
    font-weight: 700;
  }

  .service-list {
    position: absolute;
    list-style: none;
    left: 262px;
    width: 260px;
    font-size: 12.5px;
    line-height: 1.18;
    font-weight: 700;
  }
  .service-list--roofing { top: 22px; }
  .service-list--ground { top: 150px; }
  .service-list li {
    position: relative;
    padding-left: 16px;
    margin-bottom: 2px;
  }
  .service-list li::before {
    content: "";
    position: absolute;
    left: 1px; top: 2px;
    width: 5px; height: 9px;
    border-right: 2px solid var(--tick-purple);
    border-bottom: 2px solid var(--tick-purple);
    transform: rotate(40deg);
  }
</style>
</head>
<body>

  <section class="card card--services" aria-label="Card back – services">
    <div class="photo photo--muddy-car" role="img" aria-label="Photo of a mud-covered car front"></div>

    <svg class="bubble" style="left:70px;top:40px" width="200" height="120" viewBox="0 0 200 120">
      <g fill="var(--accent-purple)">
        <circle cx="45" cy="55" r="28"/><circle cx="80" cy="38" r="30"/><circle cx="120" cy="40" r="28"/>
        <circle cx="150" cy="60" r="26"/><circle cx="110" cy="75" r="28"/><circle cx="65" cy="78" r="26"/>
        <circle cx="40" cy="104" r="9"/><circle cx="24" cy="114" r="5"/>
      </g>
      <g fill="var(--cloud-white)">
        <circle cx="45" cy="55" r="24"/><circle cx="80" cy="38" r="26"/><circle cx="120" cy="40" r="24"/>
        <circle cx="150" cy="60" r="22"/><circle cx="110" cy="75" r="24"/><circle cx="65" cy="78" r="22"/>
        <ellipse cx="97" cy="58" rx="62" ry="27"/>
        <circle cx="40" cy="104" r="6"/><circle cx="24" cy="114" r="3"/>
      </g>
      <text x="97" y="52" text-anchor="middle" font-size="15">Your car</text>
      <text x="97" y="72" text-anchor="middle" font-size="15">day by day...</text>
    </svg>

    <ul class="service-list service-list--roofing">
      <li>Entertainment &amp; Courtyard Area's etc</li>
      <li>Gutter Guard Installation</li>
      <li>Full roof restoration, We Only Use Veltrano Products</li>
      <li>(Veltrano application licence, Includes a full 10 year full warrenty )</li>
    </ul>
    <ul class="service-list service-list--ground">
      <li>Driveway Cleaning</li>
      <li>Foot Path Cleaning</li>
      <li>Pebble &amp; Normal Cement</li>
      <li>Gutter Clean Out</li>
      <li>Removal of Moss &amp; Mould</li>
      <li>Moss &amp; Mould treatment is also available</li>
    </ul>
  </section>

  <section class="card card--front" aria-label="Card front – contact details">
    <div class="photo photo--foam-car" role="img" aria-label="Photo of a car covered in washing foam"></div>

    <h1 class="business-title">KT Surface Washing Water Blasting And Roof Restorations</h1>
    <p class="abn">ABN • 47 219 806 153</p>

    <svg class="bubble" style="left:40px;top:82px" width="280" height="120" viewBox="0 0 280 120">
      <g fill="var(--accent-purple)">
        <circle cx="50" cy="70" r="32"/><circle cx="90" cy="48" r="36"/><circle cx="140" cy="45" r="34"/>
        <circle cx="185" cy="62" r="30"/><circle cx="140" cy="85" r="30"/><circle cx="90" cy="88" r="28"/>
        <circle cx="234" cy="40" r="9"/><circle cx="254" cy="28" r="5.5"/>
      </g>
      <g fill="var(--cloud-white)">
        <circle cx="50" cy="70" r="28"/><circle cx="90" cy="48" r="32"/><circle cx="140" cy="45" r="30"/>
        <circle cx="185" cy="62" r="26"/><circle cx="140" cy="85" r="26"/><circle cx="90" cy="88" r="24"/>
        <ellipse cx="118" cy="68" rx="88" ry="32"/>
        <circle cx="234" cy="40" r="6"/><circle cx="254" cy="28" r="3"/>
      </g>
      <text x="118" y="74" text-anchor="middle" font-size="19">Your car at us</text>
    </svg>

    <div class="phone">
      <svg class="phone-icon" viewBox="0 0 26 26" aria-hidden="true">
        <circle cx="13" cy="13" r="11.5" fill="none" stroke="var(--ink-white)" stroke-width="2"/>
        <path d="M8.5 7.5c1-.8 2-.6 2.4.3l.9 2c.3.7 0 1.3-.6 1.7l-.7.5c.7 1.6 1.8 2.8 3.4 3.5l.5-.7c.4-.6 1-.9 1.7-.6l2 .9c.9.4 1.1 1.4.3 2.4-1 1.2-2.8 1.4-4.5.5-2.6-1.3-4.6-3.4-5.9-6-.8-1.7-.6-3.5.5-4.5z" fill="var(--ink-white)"/>
      </svg>
      <span>0417385926</span>
    </div>

    <p class="contact-lines">Contact Reid For A Free Quote<br>Cover Maitland &amp; Newcastle Region's</p>
  </section>

</body>
</html>
```